the letter head should have the logo ( may be top left), " Fenwick Ridge Institute" (may be top/middle ) and the two clinics info in a vertical column ( along the left side of the page )

Target Market(s)

other physicians and official letters

Requirements
Must have
• the info provided in the attachements

```html
<!DOCTYPE html>
<html lang="en">
<head>
<meta charset="utf-8">
<title>Fenwick Ridge Institute – Letterhead</title>
<link href="https://fonts.googleapis.com/css2?family=Lato:wght@400;700&display=swap" rel="stylesheet">
<style>
  :root {
    --backdrop: #a5a5a5;
    --paper: #ffffff;
    --accent: #b0185f;
    --ink: #2e3a46;
    --text: #3a3a3a;
  }
  * { margin: 0; padding: 0; box-sizing: border-box; }
  html, body {
    width: 1200px; height: 1200px; overflow: hidden;
    background: var(--backdrop);
    font-family: "Lato", sans-serif;
  }
  .letterhead {
    position: absolute; left: 245px; top: 115px;
    width: 714px; height: 925px;
    background: var(--paper);
  }
  .brand {
    position: absolute; right: 69px; top: 45px;
    display: flex; align-items: center; gap: 10px;
  }
  .brand-square { width: 46px; height: 46px; background: var(--ink); }
  .brand-name {
    color: var(--ink); font-weight: 400; font-size: 22px; line-height: 1.05;
  }
  .offices { position: absolute; left: 42px; top: 385px; width: 110px; }
  .office-title {
    color: var(--accent); font-weight: 700; font-size: 10.5px; margin-bottom: 5px;
  }
  .office-line {
    display: flex; align-items: flex-start; gap: 4px;
    color: var(--text); font-size: 9px; line-height: 11px;
  }
  .office-line svg { width: 7px; height: 7px; margin-top: 2px; flex: none; fill: var(--accent); }
  .office-line.address { margin-top: 3px; }
  .divider {
    height: 1px; width: 98px; margin: 22px 0 24px;
    background: linear-gradient(90deg, transparent, var(--accent) 30%, var(--accent) 70%, transparent);
  }
</style>
</head>
<body>
  <main class="letterhead">
    <header class="brand">
      <div class="brand-square"></div>
      <div class="brand-name">Fenwick Ridge<br>Institute</div>
    </header>

    <section class="offices">
      <div class="office">
        <h2 class="office-title">Harrow Bend Office</h2>
        <p class="office-line"><svg viewBox="0 0 10 10"><path d="M2 0l2 2.5-1 1.2c.6 1.4 1.8 2.6 3.3 3.3l1.2-1L10 8l-1.5 2C4 10 0 6 0 1.5z"/></svg>555-210-4817</p>
        <p class="office-line"><svg viewBox="0 0 10 10"><rect x="2" y="0" width="6" height="3"/><rect x="0" y="3.5" width="10" height="6.5"/></svg>555-210-4820</p>
        <p class="office-line address"><svg viewBox="0 0 10 10"><path d="M5 0a3.5 3.5 0 0 1 3.5 3.5C8.5 6 5 10 5 10S1.5 6 1.5 3.5A3.5 3.5 0 0 1 5 0zm0 2a1.5 1.5 0 1 0 0 3 1.5 1.5 0 0 0 0-3z"/></svg><span>218 N. Alder Ave.<br>Suite 310, 40512</span></p>
      </div>

      <div class="divider"></div>

      <div class="office">
        <h2 class="office-title">Cedar Hollow Office</h2>
        <p class="office-line"><svg viewBox="0 0 10 10"><path d="M2 0l2 2.5-1 1.2c.6 1.4 1.8 2.6 3.3 3.3l1.2-1L10 8l-1.5 2C4 10 0 6 0 1.5z"/></svg>555-384-2291</p>
        <p class="office-line"><svg viewBox="0 0 10 10"><rect x="2" y="0" width="6" height="3"/><rect x="0" y="3.5" width="10" height="6.5"/></svg>555-384-2290</p>
        <p class="office-line address"><svg viewBox="0 0 10 10"><path d="M5 0a3.5 3.5 0 0 1 3.5 3.5C8.5 6 5 10 5 10S1.5 6 1.5 3.5A3.5 3.5 0 0 1 5 0zm0 2a1.5 1.5 0 1 0 0 3 1.5 1.5 0 0 0 0-3z"/></svg><span>7420 W. Juniper St.<br>Cedar Hollow 40618</span></p>
      </div>
    </section>
  </main>
</body>
</html>
```